Quorvis Business Card

Require a business card for QuorVis. QuorVis is an aircraft engineering consultancy company.
Company is used for end of leases inspections, pre purchase inspections,asset inspections

Industry/Entity Type

Business

Contact Information for Business Card

QuorVis Limited
Miles Tandry
miles@quorvis.nz
64 (0)275918203

Requirements
Must have
• Aircraft silhouette in background

```html
<!DOCTYPE html>
<html lang="en">
<head>
<meta charset="utf-8">
<title>QuorVis Limited – Business Card</title>
<link rel="stylesheet" href="https://fonts.googleapis.com/css2?family=Orbitron:wght@500&family=Libre+Baskerville:wght@700&family=Arimo:wght@400&display=swap">
<style>
  :root {
    --page-bg: #2b2d31;
    --card-bg: #1f1f1f;
    --glow-core: #f0a02a;
    --glow-mid: #8a5a22;
    --glow-outer: rgba(70, 50, 32, 0.7);
    --silhouette: #161412;
    --accent: #e8743a;
    --text-light: #ffffff;
    --icon-bg: #e8743a;
  }
  * { margin: 0; padding: 0; box-sizing: border-box; }
  html, body {
    width: 1200px;
    height: 1000px;
    overflow: hidden;
    background: var(--page-bg);
  }
  .stage {
    width: 1200px;
    height: 1000px;
    display: flex;
    align-items: center;
    justify-content: center;
  }
  .business-card {
    position: relative;
    width: 900px;
    height: 560px;
    overflow: hidden;
    background:
      radial-gradient(ellipse 360px 300px at 58% 42%, var(--glow-core) 0%, var(--glow-mid) 35%, var(--glow-outer) 65%, rgba(31, 31, 31, 0) 100%),
      var(--card-bg);
    box-shadow: 0 20px 50px rgba(0, 0, 0, 0.5);
  }
  .aircraft-silhouette {
    position: absolute;
    left: 230px;
    top: 215px;
    width: 460px;
    height: 130px;
    border-radius: 65px;
    background: radial-gradient(ellipse at 50% 50%, var(--silhouette) 0%, rgba(22, 20, 18, 0.85) 45%, rgba(22, 20, 18, 0) 100%);
  }
  .brand {
    position: absolute;
    top: 34px;
    right: 40px;
    text-align: right;
    color: var(--accent);
    font-family: "Orbitron", sans-serif;
    font-weight: 500;
  }
  .brand-name {
    font-size: 38px;
    letter-spacing: 3px;
    text-transform: uppercase;
    line-height: 1;
  }
  .brand-tagline {
    margin-top: 6px;
    font-size: 17px;
    letter-spacing: 3px;
    line-height: 1;
  }
  .person-name {
    position: absolute;
    top: 145px;
    right: 110px;
    color: var(--text-light);
    font-family: "Libre Baskerville", serif;
    font-weight: 700;
    font-size: 40px;
    text-transform: uppercase;
    letter-spacing: 1px;
    line-height: 1.1;
  }
  .contact-list {
    position: absolute;
    left: 50px;
    bottom: 45px;
    list-style: none;
    color: var(--text-light);
    font-family: "Arimo", sans-serif;
    font-size: 42px;
    line-height: 1.1;
  }
  .contact-item {
    display: flex;
    align-items: center;
    gap: 18px;
    margin-top: 12px;
  }
  .contact-icon {
    flex: none;
    width: 30px;
    height: 30px;
  }
</style>
</head>
<body>
  <main class="stage">
    <article class="business-card">
      <div class="aircraft-silhouette" role="img" aria-label="Silhouette of a four-engine airliner flying head-on in front of the glowing orange sun"></div>

      <header class="brand">
        <p class="brand-name">QuorVis Limited</p>
        <p class="brand-tagline">Aircraft Technical Consultants</p>
      </header>

      <h1 class="person-name">Miles Tandry</h1>

      <ul class="contact-list">
        <li class="contact-item">
          <svg class="contact-icon" viewBox="0 0 30 30" aria-hidden="true">
            <rect width="30" height="30" rx="5" fill="var(--icon-bg)"/>
            <rect x="6" y="9" width="18" height="12" fill="none" stroke="#fff" stroke-width="1.8"/>
            <path d="M6 9 L15 16 L24 9" fill="none" stroke="#fff" stroke-width="1.8"/>
          </svg>
          <span class="contact-email">miles@quorvis.nz</span>
        </li>
        <li class="contact-item">
          <svg class="contact-icon" viewBox="0 0 30 30" aria-hidden="true">
            <rect width="30" height="30" rx="5" fill="var(--icon-bg)"/>
            <path d="M10 7 C8 8 7 10 8 13 C10 18 13 21 17 23 C20 24 22 23 23 21 L20 18 L17.5 19.5 C15 18 12.5 15.5 11 13 L12.5 10.5 Z" fill="#fff"/>
          </svg>
          <span class="contact-phone">64 (0)275918203</span>
        </li>
      </ul>
    </article>
  </main>
</body>
</html>
```